A Volume Worth Trading - book cover (front panel only)

I want a book cover (for print and ebook) in a distinctive, quirky style that can be repurposed for podcast artwork too. Full brief supplied.
The book is a practical, accessible handbook for anyone thinking about writing a book to build their business, with a wide range of tips and techniques to help plan, write, publishing and promote a book that’s integrated with your platform and works to build your reputation, network and credibility from day 1.
The target audience is experts in business, particularly owners of SMEs with an established online and offline platform (eg speaking, training, consulting) who want to add a book to take their business to the next level.
I want the design to be strong and distinctive, slightly quirky without being gimmicky, with the focus on typography.

Target Market(s)

Those writing a book based on their expertise to build their business

Industry/Entity Type

Publishing Company

Font styles to use
Serif
Sans Serif
Decorative

Colors

Designer to choose colors to be used in the design.

Requirements
Must have
• Commercially appealing book cover design, with application files and copyright supplied, front panel only, 5.5 x 8.5 inch format. Must work at both full size and thumbnail.
Nice to have
• A distinctive style that could be applied across other products in my portfolio.

```html
<!DOCTYPE html>
<html lang="en">
<head>
<meta charset="utf-8">
<title>A Volume Worth Trading – Front Cover</title>
<link rel="stylesheet" href="https://fonts.googleapis.com/css2?family=Caveat+Brush&family=Caveat:wght@500&family=Amatic+SC:wght@700&display=swap">
<style>
  :root {
    --backdrop: #f3f3f3;
    --paper: #e9e8e4;
    --ink: #1f1f1f;
    --accent-green: #9cbb3b;
    --pen-tone-light: #dcdbd7;
    --pen-tone-dark: #b9b8b4;
  }
  html, body {
    margin: 0;
    padding: 0;
    width: 1200px;
    height: 1200px;
    overflow: hidden;
    background: var(--backdrop);
  }
  .cover {
    position: absolute;
    left: 244px;
    top: 50px;
    width: 712px;
    height: 1100px;
    background: var(--paper);
    box-shadow: 0 2px 6px rgba(0,0,0,0.08);
    overflow: hidden;
  }
  .title {
    margin: 0;
  }
  .title-line {
    position: absolute;
    left: 0;
    width: 100%;
    text-align: center;
    font-family: "Caveat Brush", cursive;
    font-weight: 400;
    line-height: 1;
    color: var(--ink);
    letter-spacing: -2px;
  }
  .title-line--first { top: 80px; font-size: 168px; }
  .title-line--second { top: 236px; font-size: 168px; }
  .title-line--accent { top: 388px; font-size: 178px; color: var(--accent-green); }
  .subtitle {
    position: absolute;
    top: 600px;
    left: 0;
    width: 100%;
    margin: 0;
    text-align: center;
    font-family: "Amatic SC", sans-serif;
    font-weight: 700;
    font-size: 36px;
    line-height: 40px;
    letter-spacing: 3px;
    text-transform: uppercase;
    color: var(--ink);
  }
  .pen-visual {
    position: absolute;
    left: 261px;
    top: 760px;
    width: 205px;
    height: 165px;
    border-radius: 12px;
    background: linear-gradient(135deg, var(--pen-tone-light), var(--pen-tone-dark));
  }
  .author {
    position: absolute;
    top: 975px;
    left: 0;
    width: 100%;
    margin: 0;
    text-align: center;
    font-family: "Caveat", cursive;
    font-weight: 500;
    font-size: 100px;
    line-height: 1;
    color: var(--ink);
  }
</style>
</head>
<body>
  <main class="cover">
    <h1 class="title">
      <span class="title-line title-line--first">A Volume</span>
      <span class="title-line title-line--second">Worth</span>
      <span class="title-line title-line--accent">Trading</span>
    </h1>
    <p class="subtitle">Smart ways to outline and draft a book<br>that pulls its weight for your company</p>
    <div class="pen-visual" role="img" aria-label="Photograph of an uncapped black fountain pen lying diagonally beside its cap"></div>
    <p class="author">Miriam Hale</p>
  </main>
</body>
</html>
```